Lanternby Consulting Business Card Design

Business Card Design for Lanternby Consulting. Lanternby Consulting is a boutique consultancy based in Atlanta, GA., that specializes in marketing strategy, organization planning, and leadership development. We provide solutions for small businesses and startups as well as Meridex 400 companies.

http://lanternbyconsulting.example/

Target Market(s)

We provide solutions for small businesses and startups as well as Meridex 400 companies.

Industry/Entity Type

Consulting

Contact Information for Business Card

Two sided business card with priority on contact information, logo, tag line (Inspiration to Dream More, Do More, Become More)

Colors

Designer to choose colors to be used in the design.

Requirements
Must have
• contact information, logo, tag line (Inspiration to Dream More, Do More, Become More)
• Simple no over communication.
Nice to have
• I would like to see different placements of logo and creative use of both sides of the card
Should not have
• Do not put too much information on the card.

```html
<!DOCTYPE html>
<html lang="en">
<head>
<meta charset="utf-8">
<title>Lanternby Consulting — Business Card</title>
<link rel="stylesheet" href="https://fonts.googleapis.com/css2?family=Montserrat:wght@400;500;600&display=swap">
<style>
  :root {
    --navy: #1d3557;
    --navy-facet: #243e63;
    --orange: #f2922a;
    --white: #ffffff;
    --ink: #1d3557;
    --backdrop: #e9e7e3;
  }
  * { box-sizing: border-box; margin: 0; padding: 0; }
  html, body {
    width: 1200px; height: 1000px; overflow: hidden;
    background: var(--backdrop);
    font-family: "Montserrat", Arial, sans-serif;
  }
  .canvas { position: relative; width: 1200px; height: 1000px; }

  .card {
    position: absolute; width: 600px; height: 360px; overflow: hidden;
    background: var(--navy);
    box-shadow: 0 10px 24px rgba(0,0,0,0.25);
  }
  .card--front { left: 195px; top: 103px; }
  .card--back { left: 405px; top: 536px; }

  .card__shape { position: absolute; inset: 0; }

  .holder { position: absolute; left: 25px; top: 152px; width: 288px; }
  .holder__name {
    font-size: 31px; font-weight: 500; letter-spacing: 0.5px;
    color: var(--ink); white-space: nowrap;
  }
  .holder__name-last { color: var(--orange); }
  .holder__role {
    text-align: right; font-size: 15px; letter-spacing: 1px;
    color: var(--ink); margin-top: 6px;
  }

  .wordmark { position: absolute; color: var(--white); font-weight: 600; text-align: right; line-height: 1; }
  .wordmark__name { display: block; font-size: 30px; letter-spacing: 0.5px; }
  .wordmark__sub { display: block; font-size: 12px; letter-spacing: 2.5px; margin-top: 6px; }
  .card--front .wordmark { right: 24px; top: 88px; }
  .card--back .wordmark { right: 42px; top: 258px; }

  .contacts { position: absolute; right: 20px; top: 235px; list-style: none; }
  .contacts__item {
    display: flex; justify-content: flex-end; align-items: center;
    height: 25px; color: var(--orange); font-size: 14px; letter-spacing: -0.2px;
    white-space: nowrap;
  }
  .contacts__item--gap { margin-top: 4px; }
  .contacts__icon { width: 13px; height: 13px; margin-left: 16px; fill: var(--white); flex: none; }

  .tagline {
    position: absolute; left: 0; right: 0; top: 178px;
    text-align: center; color: var(--orange); font-size: 16px; letter-spacing: 0.3px;
  }
</style>
</head>
<body>
<main class="canvas">

  <section class="card card--front" aria-label="Business card front">
    <svg class="card__shape" viewBox="0 0 600 360" aria-hidden="true">
      <polygon points="275,0 422,0 348,180" fill="var(--navy-facet)"/>
      <polygon points="0,0 275,0 348,180 275,360 0,360" fill="var(--white)"/>
    </svg>

    <div class="holder">
      <p class="holder__name">NAME <span class="holder__name-last">SURNAME</span></p>
      <p class="holder__role">CONSULTING</p>
    </div>

    <p class="wordmark">
      <span class="wordmark__name">Lanternby</span>
      <span class="wordmark__sub">CONSULTING</span>
    </p>

    <ul class="contacts">
      <li class="contacts__item">404-555-0172
        <svg class="contacts__icon" viewBox="0 0 24 24" aria-hidden="true"><path d="M6.6 10.8a15.2 15.2 0 0 0 6.6 6.6l2.2-2.2a1 1 0 0 1 1-.25 11.4 11.4 0 0 0 3.6.57 1 1 0 0 1 1 1V20a1 1 0 0 1-1 1A17 17 0 0 1 3 4a1 1 0 0 1 1-1h3.5a1 1 0 0 1 1 1c0 1.25.2 2.45.57 3.6a1 1 0 0 1-.25 1z"/></svg>
      </li>
      <li class="contacts__item">lanternbyconsulting.example
        <svg class="contacts__icon" viewBox="0 0 24 24" aria-hidden="true"><circle cx="12" cy="12" r="10"/><path d="M12 2v20M2 12h20M12 2c3 3 3 17 0 20M12 2c-3 3-3 17 0 20" stroke="var(--navy)" stroke-width="1.6" fill="none"/></svg>
      </li>
      <li class="contacts__item contacts__item--gap">di@lanternbyconsulting.example
        <svg class="contacts__icon" viewBox="0 0 24 24" aria-hidden="true"><rect x="2" y="5" width="20" height="14" rx="1"/><path d="M2.5 6l9.5 7 9.5-7" stroke="var(--navy)" stroke-width="1.6" fill="none"/></svg>
      </li>
      <li class="contacts__item">4821 Birch Row 210, Atlanta, GA
        <svg class="contacts__icon" viewBox="0 0 24 24" aria-hidden="true"><path d="M12 2a7 7 0 0 0-7 7c0 5 7 13 7 13s7-8 7-13a7 7 0 0 0-7-7zm0 9.5A2.5 2.5 0 1 1 12 6.5a2.5 2.5 0 0 1 0 5z"/></svg>
      </li>
    </ul>
  </section>

  <section class="card card--back" aria-label="Business card back">
    <p class="tagline">Inspiration to Dream More, Do More, Become More</p>
    <p class="wordmark">
      <span class="wordmark__name">Lanternby</span>
      <span class="wordmark__sub">CONSULTING</span>
    </p>
  </section>

</main>
</body>
</html>
```